Every sort of trades everysortoftrades.ca

Website for company offering Every sort of trades
Welding/Fabrication/Metal repairs/Metal building, Electrical repairs and installations, Plumbing and Heating, Renovations, Flooring, Paiting, and other services

We need a very clean and professional website outlining the many services we have

We would like each type of service to have its own page, with images of those types of services on those pages.

Then in the future, we can update those pages with projects we have done of those types.

Every Sort of Trades . CA

Located in Calgary, Alberta, Canada, offering services Alberta wide

Welding/Fabrication/Repair/Building - Steel and metals
Electrical contractor - Journeyman , small or large projects
Plumbing and Heating
Renovations
Flooring
Painting
Other services - storage, trucking, delivery, etc

business and residential services

Contractor

5+ page

Sans Serif

3176b5
0253a1
85acd3
85abd2
cedeed
ffffff

Must have
• Clean
• Professional
• Easy of updating text and images

```html
<!DOCTYPE html>
<html lang="en">
<head>
<meta charset="utf-8">
<title>Every Sort of Trades</title>
<link href="https://fonts.googleapis.com/css2?family=Roboto:ital,wght@0,300;0,400;0,500;0,700;0,900;1,400&family=Dancing+Script:wght@500&display=swap" rel="stylesheet">
<style>
:root{
  --blue:#3176b5;
  --blue-deep:#0253a1;
  --blue-soft:#85acd3;
  --blue-pale:#cedeed;
  --white:#ffffff;
  --ink:#222a33;
  --grey:#5e656d;
  --light:#f1f2f4;
  --line:#3f7fc0;
}
*{box-sizing:border-box;margin:0;padding:0}
html,body{width:1200px;height:2723px;overflow:hidden}
body{font-family:'Roboto',Arial,sans-serif;color:var(--ink);background:var(--white);position:relative}
.abs{position:absolute}

/* top bar */
.topbar{left:0;top:0;width:1200px;height:35px;background:var(--blue);color:var(--white);font-weight:700}
.topbar .support{left:51px;top:9px;font-size:14px}
.topbar .estimates{left:499px;top:0;width:176px;height:35px;background:var(--blue-deep);font-size:14px;text-align:center;line-height:35px}
.topbar .call{right:51px;top:4px;font-size:13px;display:flex;align-items:baseline;gap:8px}
.topbar .call b{font-size:23px;font-weight:700}

/* header */
.header{left:0;top:35px;width:1200px;height:68px;background:var(--white)}
.brand{left:51px;top:16px;font-size:28px;font-weight:900;color:var(--blue-deep);letter-spacing:-.5px}
.nav{left:332px;top:27px;display:flex;gap:38px;font-size:12.5px;color:var(--ink);text-transform:uppercase}
.social-top{left:1062px;top:24px;display:flex;gap:22px}
.social-top span{width:14px;height:14px;border-radius:2px;display:block}

/* hero */
.hero{left:0;top:103px;width:1200px;height:489px;background:linear-gradient(100deg,#6f5b45 0%,#a08a70 28%,#8d8a86 46%,#b7bec7 62%,#d6dbe0 100%)}
.hero-circle{left:482px;top:185px;width:240px;height:240px;border-radius:50%;background:rgba(60,60,60,.28);color:var(--white);text-align:center;padding-top:80px;line-height:1.1}
.hero-circle .s{font-size:25px;font-weight:300;letter-spacing:1px}
.hero-circle .l{font-size:34px;font-weight:500;letter-spacing:1px}

/* features */
.features{left:0;top:592px;width:1200px;height:312px;background:var(--blue-deep);background-image:linear-gradient(180deg,#0b5cab,#0253a1)}
.feat-line{top:67px;height:1px;background:var(--blue-soft)}
.feature{top:20px;width:380px;text-align:center;color:var(--white)}
.feature .icon{width:94px;height:94px;border-radius:50%;background:#3aa6dc;margin:0 auto;border:3px solid rgba(255,255,255,.25)}
.feature .script{font-family:'Dancing Script',cursive;font-size:25px;margin-top:20px;line-height:1}
.feature h3{font-size:18px;font-weight:500;margin-top:3px}
.feature p{font-size:12.5px;line-height:20px;margin:18px auto 0;width:330px;color:#e7eef7}
.feature a{display:block;margin-top:14px;font-size:12px;font-weight:700;color:var(--white);text-decoration:none}

/* services */
.services{left:0;top:904px;width:1200px;height:316px;background:var(--light)}
.tabs{left:59px;top:20px;display:flex;align-items:center;gap:0}
.tab{font-size:15px;font-weight:500;color:var(--ink);padding:0 24px;height:44px;line-height:44px}
.tab.active{border:1.5px solid var(--blue);border-radius:3px;background:var(--white);color:var(--blue-deep);padding:0 20px}
.dots{height:0;border-top:2px dotted var(--blue)}
.cards{left:51px;top:111px;display:flex;gap:29px}
.card{width:252px;height:163px;border-radius:0 0 16px 16px;overflow:hidden;background:var(--white)}
.card .photo{height:120px}
.card .label{height:43px;background:linear-gradient(90deg,var(--blue-deep),var(--blue));color:var(--white);text-align:center;line-height:43px;font-size:15px}

/* projects */
.section-title{width:1200px;text-align:center;font-size:22px;font-weight:700;color:var(--ink)}
.section-title em{font-style:normal;color:var(--blue-deep)}
.grid{left:0;top:1292px;width:1200px;display:grid;grid-template-columns:repeat(5,240px);grid-template-rows:178px 189px}

/* testimonials */
.testimonials{left:0;top:1684px;width:1200px;height:358px;background:linear-gradient(90deg,#e9ecef,#f6f6f6 40%,#f3f3f3 60%,#e5e8ea)}
.quote{width:410px;font-size:12.5px;line-height:19px;font-style:italic;color:var(--grey)}
.quote.left{text-align:right}
.quote .who{display:block;font-style:normal;color:var(--ink);font-size:12.5px;margin-top:9px}
.avatar{width:76px;height:76px;border-radius:50%;border:3px solid var(--white);background:linear-gradient(160deg,#c9b8a6,#6f5b4c)}

/* contact */
.col-title{font-size:17px;font-weight:700;color:var(--ink)}
.field{border:1px solid #b9c2cc;border-radius:3px;background:var(--white);font-size:12px;color:#8a9099;padding:0 12px;line-height:31px}
.send{left:51px;top:2303px;width:136px;height:31px;background:var(--blue-deep);color:var(--white);font-size:12px;font-weight:700;text-align:center;line-height:31px;border-radius:2px}
.map{left:334px;top:2109px;width:534px;height:227px;background:linear-gradient(135deg,#e8e4da 0%,#efe9df 30%,#8eb4dc 38%,#a9c6e6 55%,#ece6d9 62%,#e2dccf 100%)}
.info{font-size:12.5px;color:var(--grey)}
.info b{font-weight:400;color:var(--blue)}
.follow{left:895px;top:2263px;display:flex;gap:8px}
.follow span{width:30px;height:30px;border-radius:50%;background:var(--blue-deep);display:block;border:7px solid var(--blue-deep);box-shadow:inset 0 0 0 8px var(--blue-deep),inset 0 0 0 30px #3d7fc4}

/* like bar */
.like-line{left:65px;top:2410px;width:1065px;height:1px;background:#e1e4e8}
.like-pill{left:378px;top:2388px;width:444px;height:44px;border-radius:22px;background:var(--white);border:1px solid #e6e8eb;display:flex;align-items:center;padding-left:20px;gap:12px;font-size:10px;color:var(--ink)}
.like-btn{background:var(--blue);color:var(--white);font-size:10px;font-weight:700;padding:3px 7px;border-radius:2px;margin-left:58px}

/* footer */
.footer{left:0;top:2450px;width:1200px;height:273px;background:linear-gradient(90deg,#0e58ab,#2d6fb8 60%,#3176b5);color:var(--white)}
.footer .brand-foot{left:120px;top:70px;font-size:26px;font-weight:900;width:140px;text-align:center;line-height:1.1}
.fcol{top:27px;width:220px;text-align:center}
.fcol h4{font-size:17px;font-weight:700;margin-bottom:10px}
.fcol li{list-style:none;font-size:13px;line-height:24.5px}
.footer .rule{left:0;top:204px;width:1200px;height:1px;background:rgba(255,255,255,.35)}
.footer .legal{left:0;top:232px;width:1200px;text-align:center;font-size:11px;font-weight:500}
</style>
</head>
<body>

<div class="abs topbar">
  <div class="abs support">24/7 Emergency Support</div>
  <div class="abs estimates">FREE ESTIMATES +</div>
  <div class="abs call">Call Today <b>403-555-0147</b></div>
</div>

<header class="abs header">
  <div class="abs brand">Every Sort of Trades</div>
  <nav class="abs nav"><span>About</span><span>Services</span><span>Gallery</span><span>Resources</span><span>Reviews</span><span>Contact</span></nav>
  <div class="abs social-top"><span style="background:#3b5a9a"></span><span style="background:#2aa3e0"></span><span style="background:#d4314a"></span></div>
</header>

<section class="abs hero" role="img" aria-label="Interior photo: wooden floor with table and chairs blending into an empty lit warehouse">
  <div class="abs hero-circle">
    <div class="s">ARE YOU</div>
    <div class="l">LOOKING</div>
    <div class="s">FOR</div>
    <div class="s">CONTRACTOR</div>
  </div>
</section>

<section class="abs features">
  <div class="abs feat-line" style="left:338px;width:149px"></div>
  <div class="abs feat-line" style="left:712px;width:148px"></div>
  <div class="abs feature" style="left:35px">
    <div class="icon" role="img" aria-label="Parachute delivery icon"></div>
    <div class="script">Innovative</div>
    <h3>Products &amp; Services</h3>
    <p>High quality in our services to your home's specifications.</p>
    <a>START NOW ›</a>
  </div>
  <div class="abs feature" style="left:409px">
    <div class="icon" role="img" aria-label="Certificate clipboard icon"></div>
    <div class="script">Trained &amp; Certified</div>
    <h3>Experts</h3>
    <p>A team of certified specialists with decades of collective experience.</p>
    <a>LEARN MORE ›</a>
  </div>
  <div class="abs feature" style="left:785px">
    <div class="icon" role="img" aria-label="Cash and card icon"></div>
    <div class="script">Custom Financing</div>
    <h3>Solutions</h3>
    <p>Flexible financing programs for your new system, on approved credit. Apply today!</p>
    <a>DETAILS ›</a>
  </div>
</section>

<section class="abs services">
  <div class="abs tabs">
    <div class="tab active">Flooring</div>
    <div class="tab">Steel and Metals</div>
    <div class="tab">Electrical contractor</div>
    <div class="tab">Renovations</div>
    <div class="tab">Plumbing and Heating</div>
    <div class="tab">Painting</div>
    <div class="tab">Other services</div>
  </div>
  <div class="abs dots" style="left:51px;top:78px;width:1096px"></div>
  <div class="abs cards">
    <div class="card"><div class="photo" role="img" aria-label="Hardwood floor photo" style="background:linear-gradient(160deg,#8a3f1c,#c67a3f 60%,#5a2a14)"></div><div class="label">Hardwood</div></div>
    <div class="card"><div class="photo" role="img" aria-label="Laminate floor installation photo" style="background:linear-gradient(160deg,#d8d3cb,#b9a58c 60%,#8c7056)"></div><div class="label">Laminate</div></div>
    <div class="card"><div class="photo" role="img" aria-label="Stone floored kitchen photo" style="background:linear-gradient(160deg,#6a5646,#a89583 55%,#4a3b30)"></div><div class="label">Stone</div></div>
    <div class="card"><div class="photo" role="img" aria-label="Marble floor with staircase photo" style="background:linear-gradient(160deg,#b49b85,#e4d8ca 55%,#7b5a43)"></div><div class="label">Marble</div></div>
  </div>
</section>

<div class="abs section-title" style="left:0;top:1230px">Latest <em>Projects</em></div>
<div class="abs grid">
  <div role="img" aria-label="Modern house with patio at dusk" style="background:linear-gradient(160deg,#3b4c63,#8b7b6a 60%,#2f3a2a)"></div>
  <div role="img" aria-label="Modern house with lawn at dusk" style="background:linear-gradient(160deg,#2e3a4e,#8a6e52 55%,#3e4a2a)"></div>
  <div role="img" aria-label="Contemporary house entrance" style="background:linear-gradient(160deg,#b9c4cf,#7a6a5b 55%,#4f4a44)"></div>
  <div role="img" aria-label="Warm wood-panelled living room" style="background:linear-gradient(160deg,#6a4424,#c48a55 55%,#3a2514)"></div>
  <div role="img" aria-label="Bungalow with garden" style="background:linear-gradient(180deg,#9ec3e6,#d9dde0 55%,#5d8a3d)"></div>
  <div role="img" aria-label="Two-storey house with stone path" style="background:linear-gradient(180deg,#8fb8e0,#c7c2b8 55%,#4e7b32)"></div>
  <div role="img" aria-label="Timber cabin in snow at night" style="background:linear-gradient(180deg,#1f2c55,#6b4a2e 55%,#c9d2e2)"></div>
  <div role="img" aria-label="White house among trees" style="background:linear-gradient(180deg,#6fa8e0,#e7e0d2 50%,#5c9a3a)"></div>
  <div role="img" aria-label="Wood and stone house with lawn" style="background:linear-gradient(180deg,#7db0de,#8a6b4e 55%,#4e8a34)"></div>
  <div role="img" aria-label="Brick house with pool at dusk" style="background:linear-gradient(180deg,#3e5a86,#9a5a3e 55%,#3e8fb0)"></div>
</div>

<section class="abs testimonials" role="img" aria-label="Faded living room backdrop">
  <div class="abs section-title" style="left:0;top:18px">What <em>People Say</em></div>
  <div class="abs dots" style="left:51px;top:59px;width:1096px;border-top-width:1.5px"></div>
  <div class="abs dots" style="left:51px;top:213px;width:1096px;border-top-width:1.5px"></div>
  <div class="abs" style="left:599px;top:76px;height:250px;border-left:1.5px dashed var(--blue)"></div>

  <div class="abs quote left" style="left:53px;top:104px">Duis aute irure dolor in reprehenderit in voluptate velit esse cillum dolore eu fugiat nulla pariatur. Excepteur sint occaecat cupidatat non proident, sunt in culpa qui officia deserunt mollit.<span class="who">Dale Corwin, Operations Manager</span></div>
  <div class="abs avatar" role="img" aria-label="Customer portrait" style="left:490px;top:106px"></div>
  <div class="abs avatar" role="img" aria-label="Customer portrait" style="left:632px;top:106px"></div>
  <div class="abs quote" style="left:739px;top:104px">Provident, similique sunt in culpa qui officia deserunt mollitia animi, id est laborum et dolorum fuga. Et harum quidem rerum facilis est et expedita distinctio. Nam libero tempore, cum soluta nobis.<span class="who">Lena Graves, Creative Designer</span></div>

  <div class="abs quote left" style="left:53px;top:242px">Luis aute irure dolor in reprehenderit in piluptate velit esse cillum dolore eu fugiat nulla pariatur. Excepteur sint occaecat cupidatat non proident, sunt in culpa qui officia deserunt mollit.<span class="who">Marla Lind, Manager</span></div>
  <div class="abs avatar" role="img" aria-label="Customer portrait" style="left:490px;top:240px"></div>
  <div class="abs avatar" role="img" aria-label="Customer portrait" style="left:632px;top:240px"></div>
  <div class="abs quote" style="left:739px;top:242px">At vero eos et accusamus et iusto odio dignissimos ducimus qui blanditiis praesentium voluptatum deleniti atque corrupti quos dolores et quas molestias excepturi sint occaecati asperiores.<span class="who">Tim Larkin, Developer</span></div>
</section>

<div class="abs col-title" style="left:51px;top:2064px">Feel Free to Mail</div>
<div class="abs field" style="left:51px;top:2111px;width:118px">Name *</div>
<div class="abs field" style="left:187px;top:2111px;width:118px">Email *</div>
<div class="abs field" style="left:51px;top:2162px;width:254px">Subject</div>
<div class="abs field" style="left:51px;top:2212px;width:254px;height:70px">Write Your Message Here...</div>
<div class="abs send">SEND MESSAGE</div>

<div class="abs col-title" style="left:334px;top:2070px;width:534px;text-align:center">Headquarters</div>
<div class="abs map" role="img" aria-label="Street map showing the headquarters location by the harbour"></div>

<div class="abs col-title" style="left:895px;top:2064px">Contact Info</div>
<div class="abs info" style="left:895px;top:2105px">Phone: <b>+1 (800) 555 0196</b></div>
<div class="abs info" style="left:895px;top:2139px">Office: <b>Bow River Trade Centre</b></div>
<div class="abs info" style="left:895px;top:2172px">Email: <b>info@everysortoftrades.ca</b></div>
<div class="abs col-title" style="left:895px;top:2221px">Follow Us on</div>
<div class="abs follow"><span></span><span></span><span></span><span></span><span></span></div>

<div class="abs like-line"></div>
<div class="abs like-pill">
  <svg width="18" height="16" viewBox="0 0 18 16"><path d="M1 7h3v8H1zM5 7l4-6c1.5 0 2 1 1.6 2.4L10 6h5.5c1 0 1.7.9 1.4 1.9l-1.6 6c-.2.7-.9 1.1-1.6 1.1H5z" fill="#c9cdd2"/></svg>
  <span class="like-btn">✓ Like</span><span>You and 4k others like this.</span>
</div>

<footer class="abs footer">
  <div class="abs brand-foot">Every Sort of Trades</div>
  <div class="abs fcol" style="left:349px"><h4>Quick Links</h4><ul><li>About</li><li>Our Expertise</li><li>Our Service Area</li><li>Why Choose Every Sort</li></ul></div>
  <div class="abs fcol" style="left:631px"><h4>Resources</h4><ul><li>Savings</li><li>FAQs</li><li>Safety Tips</li><li>Social Page</li></ul></div>
  <div class="abs fcol" style="left:912px"><h4>Results</h4><ul><li>Customer Reviews</li><li>Write a Review</li><li>Testimonials</li><li>Gallery</li></ul></div>
  <div class="abs rule"></div>
  <div class="abs legal">Terms and Conditions | Privacy Policy © 2017 Every Sort of Trades. All rights reserved.</div>
</footer>

</body>
</html>
```